I am looking for help designing my new business cards. I would like rounded edges and a raised logo on the back of the card. I have 2 Logos. One with a boat in it and one without. I'd like the one on the back to be the one that includes the boat and just the name on the front. I have included multiple formats of my logo. Please let me know if you need anymore.

Target Market(s)

Potential buyers and other sales brokers

Industry/Entity Type

Sales - Yacht / Boat Sales

Contact Information for Business Card

Id liike the front to include just the business name portion of the logo along with my name (Corwin Dalby), phone number (555.318.6027), website address (www.dalbymarineco.example) and not my physical address but just "Port Alder, NC". The back should include my full logo that has the boat included. This portion I'd prefer raised amd take up the majority of the space there. Thanks!!

Colors
0054AA
0677BA
7BADD7
CADEEF
E8F1F8
0094D4
00A9DD
6FCCEA
C7EBF8
E9F6FB

Requirements
Must have
• Double sided
Nice to have
• My email address: Corwin@dalbymarineco.example The NMTG logo somewhere small on the front of the card
Should not have
• My full address, prefer only "Port Alder, NC"

```html
<!DOCTYPE html>
<html lang="en">
<head>
<meta charset="utf-8">
<title>Dalby Marine Co — Business Card</title>
<link href="https://fonts.googleapis.com/css2?family=Montserrat:wght@400;700;800&display=swap" rel="stylesheet">
<style>
  :root{
    --page:#ffffff;
    --card-light:#E8F1F8;
    --sea:#0094D4;
    --navy:#0B2C66;
    --deep:#0054AA;
    --sky:#6FCCEA;
    --mist:#C7EBF8;
    --white:#ffffff;
  }
  *{box-sizing:border-box;margin:0;padding:0}
  html,body{width:1200px;height:1200px;overflow:hidden;background:var(--page)}
  body{position:relative;font-family:"Montserrat",sans-serif}
  .card{
    position:absolute;left:204px;width:792px;height:452px;
    border-radius:56px;overflow:hidden;background:var(--card-light);
    box-shadow:0 14px 30px rgba(0,0,0,.18);
  }
  .card--front{top:93px}
  .card--back{top:643px}
  .band{position:absolute;inset:0;width:100%;height:100%}
  .wordmark{position:absolute;color:var(--navy);font-weight:800;text-align:center;line-height:1}
  .wordmark__name{display:block;letter-spacing:.05em}
  .wordmark__sub{display:block;letter-spacing:.24em}
  .card--front .wordmark{left:58px;top:36px;width:274px}
  .card--front .wordmark__name{font-size:58px}
  .card--front .wordmark__sub{font-size:17px;margin-top:6px}
  .holder{position:absolute;left:55px;top:285px;color:var(--white);font-weight:700;font-size:33px;letter-spacing:.01em;white-space:nowrap}
  .contact{position:absolute;left:470px;top:257px;list-style:none;color:var(--white);font-size:18px;font-weight:400}
  .contact li{display:flex;align-items:center;height:34px}
  .contact svg{width:21px;height:21px;margin-right:12px;fill:var(--white)}
  .boat-art{
    position:absolute;left:233px;top:18px;width:323px;height:146px;border-radius:24px;
    background:linear-gradient(180deg,rgba(11,44,102,.10),rgba(0,148,212,.35));
  }
  .card--back .wordmark{left:226px;top:174px;width:340px}
  .card--back .wordmark__name{font-size:70px}
  .card--back .wordmark__sub{font-size:21px;margin-top:8px}
</style>
</head>
<body>

<section class="card card--front">
  <svg class="band" viewBox="0 0 792 452" preserveAspectRatio="none" aria-hidden="true">
    <path d="M0 110 C200 140 420 95 792 120 L792 452 L0 452 Z" fill="var(--mist)"/>
    <path d="M0 128 C200 160 420 112 792 140 L792 452 L0 452 Z" fill="var(--sky)"/>
    <path d="M0 150 C200 182 420 132 792 162 L792 452 L0 452 Z" fill="var(--deep)"/>
    <path d="M0 160 C200 192 420 142 792 172 L792 452 L0 452 Z" fill="var(--sea)"/>
  </svg>
  <div class="wordmark">
    <span class="wordmark__name">DALBY</span>
    <span class="wordmark__sub">MARINE CO</span>
  </div>
  <h1 class="holder">CORWIN DALBY</h1>
  <ul class="contact">
    <li><svg viewBox="0 0 24 24"><path d="M6.6 10.8a15 15 0 0 0 6.6 6.6l2.2-2.2a1 1 0 0 1 1-.25 11.4 11.4 0 0 0 3.6.57 1 1 0 0 1 1 1V20a1 1 0 0 1-1 1A17 17 0 0 1 3 4a1 1 0 0 1 1-1h3.5a1 1 0 0 1 1 1c0 1.25.2 2.45.57 3.57a1 1 0 0 1-.25 1z"/></svg>555.318.6027</li>
    <li><svg viewBox="0 0 24 24"><path d="M12 2a10 10 0 1 0 0 20 10 10 0 0 0 0-20zm6.9 6h-3a15.7 15.7 0 0 0-1.4-3.6A8 8 0 0 1 18.9 8zM12 4c.8 1.2 1.5 2.5 1.9 4h-3.8c.4-1.5 1.1-2.8 1.9-4zM4.3 14a8 8 0 0 1 0-4h3.4a16 16 0 0 0 0 4zm.8 2h3a15.7 15.7 0 0 0 1.4 3.6A8 8 0 0 1 5.1 16zm3-8h-3a8 8 0 0 1 4.4-3.6A15.7 15.7 0 0 0 8.1 8zM12 20c-.8-1.2-1.5-2.5-1.9-4h3.8c-.4 1.5-1.1 2.8-1.9 4zm2.3-6H9.7a14.7 14.7 0 0 1 0-4h4.6a14.7 14.7 0 0 1 0 4zm.2 5.6a15.7 15.7 0 0 0 1.4-3.6h3a8 8 0 0 1-4.4 3.6zm1.8-5.6a16 16 0 0 0 0-4h3.4a8 8 0 0 1 0 4z"/></svg>www.dalbymarineco.example</li>
    <li><svg viewBox="0 0 24 24"><path d="M10 20v-6h4v6h5v-8h3L12 3 2 12h3v8z"/></svg>Port Alder, NC</li>
  </ul>
</section>

<section class="card card--back">
  <div class="boat-art" role="img" aria-label="Line illustration of a center-console fishing boat riding a wave"></div>
  <div class="wordmark">
    <span class="wordmark__name">DALBY</span>
    <span class="wordmark__sub">MARINE CO</span>
  </div>
  <svg class="band" viewBox="0 0 792 452" preserveAspectRatio="none" aria-hidden="true">
    <path d="M0 282 C260 300 520 262 792 290 L792 452 L0 452 Z" fill="var(--mist)"/>
    <path d="M0 298 C260 318 520 278 792 306 L792 452 L0 452 Z" fill="var(--sky)"/>
    <path d="M0 318 C260 340 520 298 792 326 L792 452 L0 452 Z" fill="var(--deep)"/>
    <path d="M0 328 C260 350 520 308 792 336 L792 452 L0 452 Z" fill="var(--sea)"/>
  </svg>
</section>

</body>
</html>
```